Slick Web Design for Health Care Software Company

We need a new corporate web design for our company, "Brivora." We specialize in web-based cloud software geared toward helping health care professionals.

Our focus for our home site is our products and services. We want potential clients and medical boards who visit our site to have an immediate sense of professionalism and know-how. Our products are innovative, easy to use, and customizable. Users should get this feel when visiting our site.

This is a link to our previous site: www.brivorainc.example. This site is too busy, the colors are too dark, and there's too much information in each page. When creating a design, feel free to eliminate the plethora of info present in the old site.

We have a logo and content for our site that we're going to use. For each of the 7-10 products and services, there is going to be a short 1-2 paragraph excerpt on their own page, as well as a case study related to each. Other parts that can be integrated into the site are our portfolio of clients, newsletter, and about us/contact us.

Some websites to use as general inspiration:
http://www.quellsite.example/
http://www.vantrex.example/
http://www.telmaroplans.example/

Target Market(s)

Health Care Professionals from Specialty Organizations and Boards

Industry/Entity Type

Health Care

Requirements
Nice to have
• Our trademark slogan is "Turn data in knowledge, knowledge into improvement." It would be pretty sweet to integrate this idea into the design of the site.

Also, BE CREATIVE. AVOID TRADITIONAL DESIGNS. Try to exemplify innovation within clarity.
Should not have
• Avoid dark backgrounds.

```html
<!DOCTYPE html>
<html lang="en">
<head>
<meta charset="utf-8">
<title>Brivora – Home</title>
<link rel="stylesheet" href="https://fonts.googleapis.com/css2?family=Arimo:wght@400;700&display=swap">
<style>
  :root {
    --sky: #aeeaf9;
    --bubble-green: #3ccf7a;
    --bubble-teal: #2aa68a;
    --bubble-ring: #3fa8f0;
    --pill-blue: #0a3fcc;
    --pill-blue-light: #1d5cf0;
    --pill-blue-dark: #062a9a;
    --home-green: #1e6a30;
    --home-green-dark: #0f4a1c;
    --band-yellow: #f7c800;
    --band-yellow-light: #ffe04a;
    --band-edge: #d9a800;
    --ink: #000000;
    --label: #ffffff;
  }
  * { margin: 0; padding: 0; box-sizing: border-box; }
  html, body { width: 1200px; height: 967px; overflow: hidden; background: var(--sky); }
  body { font-family: "Arimo", Arial, sans-serif; color: var(--ink); }
  .page { position: relative; width: 1200px; height: 967px; background: var(--sky); overflow: hidden; }
  .bubble-field {
    position: absolute; border-radius: 50%;
    background: radial-gradient(circle at 50% 50%, var(--bubble-green) 0%, var(--bubble-teal) 55%, rgba(63,168,240,0.55) 72%, rgba(174,234,249,0) 100%);
    opacity: 0.75;
  }
  .bubble-field.top-left { left: -20px; top: -30px; width: 330px; height: 200px; }
  .bubble-field.mid { left: 460px; top: 300px; width: 560px; height: 340px; }
  .bubble-field.right { left: 860px; top: 640px; width: 360px; height: 260px; }
  .nav-pills { position: absolute; left: 0; top: 0; }
  .brand { position: absolute; left: 30px; top: 626px; display: flex; align-items: center; gap: 40px; }
  .brand-dot { width: 170px; height: 170px; border-radius: 50%; background: var(--band-yellow); }
  .brand-name { font-weight: 700; font-size: 150px; line-height: 1; letter-spacing: -3px; color: var(--ink); }
  .tagline { position: absolute; left: 376px; top: 764px; font-weight: 700; font-size: 33px; color: var(--ink); }
  .footer-band {
    position: absolute; left: 2px; top: 859px; width: 1196px; height: 106px; border-radius: 53px;
    background: linear-gradient(180deg, var(--band-yellow-light) 0%, var(--band-yellow) 45%, var(--band-edge) 100%);
    box-shadow: inset 0 -3px 6px rgba(0,0,0,0.15);
  }
  .footer-links { position: absolute; top: 20px; font-size: 26px; }
  .footer-links.left { left: 43px; }
  .footer-links.right { right: 40px; }
  .footer-links a { color: var(--ink); text-decoration: underline; }
  .copyright { position: absolute; top: 68px; width: 100%; text-align: center; font-size: 25px; }
  .pill-label { font-family: "Arimo", Arial, sans-serif; font-weight: 700; font-size: 44px; fill: var(--label); letter-spacing: 1px; }
</style>
</head>
<body>
<main class="page">
  <div class="bubble-field top-left" role="img" aria-label="Scattered green and blue bubble pattern"></div>
  <div class="bubble-field mid" role="img" aria-label="Scattered green and blue bubble pattern"></div>
  <div class="bubble-field right" role="img" aria-label="Scattered green and blue bubble pattern"></div>

  <svg class="nav-pills" width="1200" height="967" viewBox="0 0 1200 967">
    <defs>
      <linearGradient id="pillFill" x1="0" x2="1" y1="0" y2="0">
        <stop offset="0" stop-color="var(--pill-blue-dark)"/>
        <stop offset="0.35" stop-color="var(--pill-blue-light)"/>
        <stop offset="1" stop-color="var(--pill-blue)"/>
      </linearGradient>
      <radialGradient id="homeFill" cx="0.45" cy="0.35" r="0.7">
        <stop offset="0" stop-color="var(--home-green)"/>
        <stop offset="1" stop-color="var(--home-green-dark)"/>
      </radialGradient>
      <path id="arc-about" d="M81.5 373.5 L81.5 523.5 A64 64 0 0 0 209.5 523.5 L209.5 373.5"/>
      <path id="arc-services" d="M229.5 318.5 L229.5 468.5 A64 64 0 0 0 357.5 468.5 L357.5 318.5"/>
      <path id="arc-products" d="M376.5 263.5 L376.5 413.5 A64 64 0 0 0 504.5 413.5 L504.5 263.5"/>
      <path id="arc-resources" d="M701.5 263.5 L701.5 413.5 A64 64 0 0 0 829.5 413.5 L829.5 263.5"/>
      <path id="arc-search" d="M850.5 323.5 L850.5 473.5 A64 64 0 0 0 978.5 473.5 L978.5 323.5"/>
      <path id="arc-contact" d="M998.5 378.5 L998.5 528.5 A64 64 0 0 0 1126.5 528.5 L1126.5 378.5"/>
      <path id="arc-home" d="M535 331 A68 68 0 0 0 671 331"/>
    </defs>

    <g class="pill">
      <rect x="73" y="179" width="145" height="417" rx="72.5" fill="url(#pillFill)"/>
      <text class="pill-label"><textPath href="#arc-about" startOffset="50%" text-anchor="middle">About Us</textPath></text>
    </g>
    <g class="pill">
      <rect x="221" y="126" width="145" height="415" rx="72.5" fill="url(#pillFill)"/>
      <text class="pill-label"><textPath href="#arc-services" startOffset="50%" text-anchor="middle">Services</textPath></text>
    </g>
    <g class="pill">
      <rect x="368" y="72" width="145" height="414" rx="72.5" fill="url(#pillFill)"/>
      <text class="pill-label"><textPath href="#arc-products" startOffset="50%" text-anchor="middle">Products</textPath></text>
    </g>
    <g class="pill home">
      <circle cx="603" cy="351" r="80" fill="url(#homeFill)"/>
      <text class="pill-label"><textPath href="#arc-home" startOffset="50%" text-anchor="middle">Home</textPath></text>
    </g>
    <g class="pill">
      <rect x="693" y="73" width="145" height="413" rx="72.5" fill="url(#pillFill)"/>
      <text class="pill-label"><textPath href="#arc-resources" startOffset="50%" text-anchor="middle">Resources</textPath></text>
    </g>
    <g class="pill">
      <rect x="842" y="131" width="145" height="415" rx="72.5" fill="url(#pillFill)"/>
      <text class="pill-label"><textPath href="#arc-search" startOffset="50%" text-anchor="middle">Search</textPath></text>
    </g>
    <g class="pill">
      <rect x="990" y="186" width="145" height="415" rx="72.5" fill="url(#pillFill)"/>
      <text class="pill-label"><textPath href="#arc-contact" startOffset="50%" text-anchor="middle">Contact Us</textPath></text>
    </g>
  </svg>

  <div class="brand">
    <span class="brand-dot"></span>
    <span class="brand-name">Brivora</span>
  </div>
  <p class="tagline">providing web-based solutions in health care</p>

  <footer class="footer-band">
    <nav class="footer-links left"><a href="#">Home</a> | <a href="#">About Us</a> | <a href="#">Services</a></nav>
    <nav class="footer-links right"><a href="#">Products</a> | <a href="#">Resources</a> | <a href="#">Contact Us</a></nav>
    <p class="copyright">Copy Right Brivora Inc. 2013.</p>
  </footer>
</main>
</body>
</html>
```